Personal Injury Billboard for a law frim

Our firm has a billboard we need art for. It will specifically for personal injury cases. The dimensions of art the billboard are 9 ft high 29 feet wide.

We want to highlight the terms, "Serious Injuries" and "Trusted. Local. Experienced." We want to incorporate the attached "Vantor Advocates" badge as well as our attached firm logo. We want the blue color scheme (see attached).

Maybe an image of an industrial plant in the background?

Font styles to use
Sans Serif

Colors

Designer to choose colors to be used in the design.

```html
<!DOCTYPE html>
<html lang="en">
<head>
<meta charset="utf-8">
<title>Serious Injuries Billboard</title>
<link rel="stylesheet" href="https://fonts.googleapis.com/css2?family=Archivo+Black&family=Montserrat:wght@500;600;800&display=swap">
<style>
  :root {
    --page: #ffffff;
    --panel-light: #eeeeee;
    --panel-mid: #d3d3d3;
    --blue-bright: #0a8ae6;
    --blue-mid: #1467c4;
    --blue-deep: #0b3c8c;
    --navy: #0c2f72;
    --sky-haze: #e2e5e9;
    --plant-mid: #b9bcbf;
    --plant-low: #8e8a82;
    --team-top: #6d5a52;
    --team-mid: #2f3440;
    --team-low: #1c1f27;
    --ink: #1b1b1b;
    --white: #ffffff;
  }
  html, body {
    margin: 0;
    width: 1200px;
    height: 1062px;
    overflow: hidden;
    background: var(--page);
  }
  .billboard {
    position: absolute;
    left: 31px;
    top: 355px;
    width: 1138px;
    height: 352px;
    display: block;
  }
  .tagline { font-family: "Archivo Black", sans-serif; font-size: 23px; fill: var(--blue-mid); }
  .headline { font-family: "Archivo Black", sans-serif; font-size: 98px; }
  .firm-name { font-family: "Montserrat", sans-serif; font-weight: 600; font-size: 13px; fill: var(--ink); }
  .firm-sub { font-family: "Montserrat", sans-serif; font-weight: 600; font-size: 6.5px; fill: var(--ink); letter-spacing: 1px; }
  .firm-url { font-family: "Montserrat", sans-serif; font-weight: 500; font-size: 10px; fill: var(--blue-mid); }
  .phone { font-family: "Montserrat", sans-serif; font-weight: 800; font-size: 37px; fill: var(--white); }
  .web { font-family: "Montserrat", sans-serif; font-weight: 600; font-size: 20px; fill: var(--white); letter-spacing: 1.5px; }
</style>
</head>
<body>
<svg class="billboard" viewBox="0 0 1138 352" xmlns="http://www.w3.org/2000/svg">
  <defs>
    <linearGradient id="panelGrad" x1="0" y1="0" x2="1" y2="1">
      <stop offset="0" stop-color="var(--panel-mid)"/>
      <stop offset="0.4" stop-color="var(--panel-light)"/>
      <stop offset="1" stop-color="var(--panel-light)"/>
    </linearGradient>
    <linearGradient id="swooshGrad" x1="0" y1="0" x2="1" y2="0">
      <stop offset="0" stop-color="var(--blue-mid)"/>
      <stop offset="1" stop-color="var(--blue-bright)"/>
    </linearGradient>
    <linearGradient id="plantGrad" x1="0" y1="0" x2="0" y2="1">
      <stop offset="0" stop-color="var(--sky-haze)"/>
      <stop offset="0.5" stop-color="var(--plant-mid)"/>
      <stop offset="1" stop-color="var(--plant-low)"/>
    </linearGradient>
    <linearGradient id="headGrad" x1="0" y1="0" x2="1" y2="1">
      <stop offset="0" stop-color="#3a8ad0"/>
      <stop offset="1" stop-color="var(--navy)"/>
    </linearGradient>
    <linearGradient id="bandGrad" x1="0" y1="0" x2="1" y2="0">
      <stop offset="0" stop-color="var(--blue-deep)"/>
      <stop offset="0.6" stop-color="var(--blue-mid)"/>
      <stop offset="1" stop-color="var(--blue-bright)"/>
    </linearGradient>
    <linearGradient id="teamGrad" x1="0" y1="0" x2="0" y2="1">
      <stop offset="0" stop-color="var(--team-top)"/>
      <stop offset="0.45" stop-color="var(--team-mid)"/>
      <stop offset="1" stop-color="var(--team-low)"/>
    </linearGradient>
  </defs>

  <rect class="panel" width="1138" height="352" fill="url(#panelGrad)"/>

  <path class="plant-scene" role="img" aria-label="Hazy industrial refinery with towers and smokestacks"
        fill="url(#plantGrad)" d="M580 0 H1138 V352 H370 Z"/>

  <path class="blue-swoosh" fill="url(#swooshGrad)"
        d="M242 0 H355 Q425 40 385 115 L200 352 H160 L330 125 Q380 55 242 0 Z"/>

  <g class="firm-mark">
    <rect x="106" y="38" width="44" height="44" fill="var(--blue-mid)"/>
    <text class="firm-url" x="128" y="117" text-anchor="middle">www.hor-law.com</text>
    <text class="firm-name" x="128" y="132" text-anchor="middle">HALVERN OSTBY REYES</text>
    <line x1="46" y1="139" x2="96" y2="139" stroke="var(--ink)" stroke-width="0.8"/>
    <text class="firm-sub" x="128" y="142" text-anchor="middle">ATTORNEYS</text>
    <line x1="160" y1="139" x2="211" y2="139" stroke="var(--ink)" stroke-width="0.8"/>
  </g>

  <rect class="team-photo" role="img" aria-label="Group portrait of the firm's five attorneys in suits"
        x="0" y="150" width="490" height="202" fill="url(#teamGrad)"/>

  <text class="tagline" x="604" y="70" textLength="393" lengthAdjust="spacingAndGlyphs">TRUSTED. LOCAL. EXPERIENCED</text>
  <text class="headline" x="604" y="155" fill="url(#headGrad)" textLength="395" lengthAdjust="spacingAndGlyphs">SERIOUS</text>
  <text class="headline" x="604" y="237" fill="url(#headGrad)" textLength="400" lengthAdjust="spacingAndGlyphs">INJURIES</text>

  <path class="contact-band" fill="url(#bandGrad)" d="M490 272 H880 L1064 352 H490 Z"/>
  <text class="phone" x="539" y="316" textLength="334" lengthAdjust="spacingAndGlyphs">+1 555-014-2290</text>
  <text class="web" x="588" y="341" textLength="287" lengthAdjust="spacingAndGlyphs">WWW.HOR-LAW.COM</text>
</svg>
</body>
</html>
```